Quote Cards for Social Media RV

I would like to put these quotes over one of the pictures attached; One Quote per picture, and I want the quote to be bold or easy to read as well. I provided a few reference graphics that I really like as examples below. In very small letters at the bottom add @RVCarloweDaily

All of the pictures are attached; you can pick any photo and add one quote to it; but no stock photography

Target Market(s)

women trying to lose weight

Requirements
Must have
• quotes and pictures attached
Should not have
• no stock photography

```html
<!DOCTYPE html>
<html lang="en">
<head>
<meta charset="UTF-8">
<title>Quote Card – Natural Belly Solution</title>
<link href="https://fonts.googleapis.com/css2?family=Montserrat:wght@400;500&display=swap" rel="stylesheet">
<style>
  :root {
    --card-pink: #FF9BCB;
    --quote-magenta: #CF0064;
  }
  html, body {
    margin: 0;
    padding: 0;
    width: 1200px;
    height: 1200px;
    overflow: hidden;
    background: var(--card-pink);
  }
  .quote-card {
    position: relative;
    width: 1200px;
    height: 1200px;
    background: var(--card-pink);
    font-family: "Montserrat", sans-serif;
    color: var(--quote-magenta);
  }
  .quote-card__text {
    position: absolute;
    left: 94px;
    right: 60px;
    top: 350px;
    margin: 0;
    font-size: 99px;
    line-height: 122px;
    font-weight: 400;
    letter-spacing: 0;
  }
  .quote-card__line {
    display: block;
    white-space: nowrap;
  }
  .quote-card__handle {
    position: absolute;
    left: 0;
    right: 0;
    top: 1112px;
    text-align: center;
    font-size: 27px;
    font-weight: 400;
    margin: 0;
  }
</style>
</head>
<body>
  <main class="quote-card">
    <p class="quote-card__text">
      <span class="quote-card__line">Finally-a natural</span>
      <span class="quote-card__line">solution that flattens</span>
      <span class="quote-card__line">your belly AND eases</span>
      <span class="quote-card__line">stomach bloat</span>
    </p>
    <p class="quote-card__handle">@RVCarloweDaily</p>
  </main>
</body>
</html>
```